Need innovative card design for tech start up

We are a Santa Monica based marketing analytics software start up called Meridel Pulse. We're launching a platform that will help advertisers better measure and optimize their marketing spend by using advanced algorithmic analytic. While our subject matter is complicated, we want to convey simple, clean, curated. We also want to stand out - ad tech is a sea of sameness and we need to have some individuality. We have an established color palette and would like to see a design we could print in each tone (teal, tangerine, grey), but it doesn't require the card to be monochromatic. The font used is DENSE.

Marketing

```html
<!DOCTYPE html>
<html lang="en">
<head>
<meta charset="utf-8">
<title>Meridel Pulse – Business Card</title>
<link rel="stylesheet" href="https://fonts.googleapis.com/css2?family=Oswald:wght@300;400;500&display=swap">
<style>
  :root {
    --brand-yellow: #fbc010;
    --card-white: #ffffff;
    --page-bg: #ffffff;
    --wordmark-grey: #8c8c8c;
    --text-grey: #5a5a5a;
    --card-edge: #3a3a3a;
    --accent-square: #e6e6e6;
  }

  * { box-sizing: border-box; margin: 0; padding: 0; }

  html, body {
    width: 1018px;
    height: 1200px;
    overflow: hidden;
    background: var(--page-bg);
  }

  body {
    position: relative;
    font-family: "Oswald", "Arial Narrow", sans-serif;
    font-weight: 300;
    color: var(--text-grey);
  }

  .card {
    position: absolute;
    left: 32px;
    width: 916px;
    height: 523px;
    border: 1.5px solid var(--card-edge);
    border-radius: 36px;
    background: var(--card-white);
    overflow: hidden;
  }

  .card--front { top: 36px; }
  .card--back  { top: 602px; }

  .card__band {
    position: absolute;
    left: 0;
    top: 0;
    width: 100%;
    height: 253px;
    background: var(--brand-yellow);
  }

  /* Front */
  .holder {
    position: absolute;
    left: 33px;
    top: 148px;
    color: var(--card-white);
  }

  .holder__name {
    font-weight: 500;
    font-size: 34px;
    line-height: 1.1;
    letter-spacing: 0.2px;
  }

  .holder__title {
    font-weight: 300;
    font-size: 25px;
    line-height: 1.4;
  }

  .contact {
    position: absolute;
    left: 33px;
    top: 262px;
    list-style: none;
    font-size: 25px;
    line-height: 43.5px;
    color: var(--text-grey);
  }

  .contact__label {
    color: var(--brand-yellow);
    font-weight: 400;
    margin-right: 8px;
  }

  .wordmark {
    position: absolute;
    display: flex;
    align-items: center;
    gap: 14px;
    font-size: 58px;
    font-weight: 300;
    line-height: 1;
    letter-spacing: 0.5px;
    color: var(--wordmark-grey);
    text-transform: uppercase;
    white-space: nowrap;
  }

  .wordmark__square {
    width: 34px;
    height: 34px;
    background: var(--brand-yellow);
    flex: none;
  }

  .card--front .wordmark {
    right: 32px;
    top: 276px;
  }

  /* Back */
  .card--back .wordmark {
    left: 50%;
    top: 285px;
    transform: translateX(-50%);
  }

  .website {
    position: absolute;
    left: 0;
    width: 100%;
    top: 452px;
    text-align: center;
    font-size: 25px;
    color: var(--text-grey);
  }
</style>
</head>
<body>

  <section class="card card--front" aria-label="Business card front">
    <div class="card__band"></div>

    <div class="holder">
      <p class="holder__name">Dorian Kessvale</p>
      <p class="holder__title">Founder/CEO</p>
    </div>

    <ul class="contact">
      <li>1482 Harbor Crest, suite 310</li>
      <li>Santa Monica, CA 90401</li>
      <li><span class="contact__label">office:</span> 310-555-0147 x102</li>
      <li><span class="contact__label">mobile:</span> 310-555-0193</li>
      <li>dorian@meridelpulse.com</li>
    </ul>

    <div class="wordmark">
      <span class="wordmark__square" aria-hidden="true"></span>
      <span class="wordmark__name">Meridel Pulse</span>
    </div>
  </section>

  <section class="card card--back" aria-label="Business card back">
    <div class="card__band"></div>

    <div class="wordmark">
      <span class="wordmark__square" aria-hidden="true"></span>
      <span class="wordmark__name">Meridel Pulse</span>
    </div>

    <p class="website">www.meridelpulse.com</p>
  </section>

</body>
</html>
```